Design Creative Banner or Gif Ads. 3 Designs To Be Selected

Come up with some creative banner ads for stonewell.co.nz

*At least 3 different winning banners will be chosen*

Please provide banner ads / gif ads in common google ads / website banner formats.

They can be gif or static but must stand out while still maintaining clear clean text and visuals, with a premium professional feel (please avoid clip art or anything that gives a cheap message).

Please keep in mind that these will likely be small ads so text needs to be large and if there's there a lot of text then use multiple frames/ pages as submit as a gif.

Style
Minimal & clean lines
Architectural or realistic images
Avoid cartoon styles, clipart, or anything that looks cheap

Font
Nexa or Montserrat or similar

Tone
Premium, serious, trustworthy — fits new builds

Colours
Option 1: Deep Navy (trust & quality) & lighter blues and warm grey
Option 2: Open to bright colours to help the ads stand out, such as (but not limited to) bright pink with black, yellow, fluorescent green, provided the messaging is still done professionally.
Our logo is attached (Stone Well Logo)

Display Sizes
Ad specs for file sizes should be file formats like JPEG, GIF, and PNG, with animations limited to a max of 30 seconds or less.
We will need several different ad sizes provided for each of the 3 selected winning designs.

• Medium Rectangle: 300 × 250 pixels
• Leaderboard: 728 × 90 pixels
• Desktop Banner ad image: (640x360 pixels)
• Desktop Banner ad image 2: (300x600 pixels)
• Possibly one or two other sizes

Flexibility to be creative
The ad text, words, upper/lower case, layout, colour, theme, and images can be adjusted to how you think it will look best. The follow example ads are just examples of what we are after but we are keen to see what you can create.

Recommendations at this point:
1. Avoid text heavy
2. Looking for more Gif ads
3. Imaging: if possible use real stock photo's rather than AI

Themes:

1
Building Soon? Start Here
Free Build Planning Pack:
✓ Build Cost Calculator
✓ Hidden Cost Checklist
✓ Builder Comparison Guide
Build With Confidence
Download Free

2
Before You Choose A Builder
Compare Price, Scope, Risk & Value
Avoid Costly Mistakes
Choose The Right Builder With Confidence
Download The Free Guide

3
Planning A New Build?
Avoid These Common Mistakes:
✗ Hidden Exclusions
✗ Missing Scope
✗ Unrealistic Allowances
✗ Budget Blowouts
Download The Free Guide

4
Before You Buy Land
Know what it could cost to build.
Avoid Costly Building Mistakes
Download Our Free Guides

5
Know Your Build Budget?
• Free Build Cost Calculator
• Hidden Cost Checklist
• Build Planning Tools
Calculate Costs (Download)

Target Market(s)

Landowners looking to build

Industry/Entity Type

Building

Font styles to use
Other font styles liked:
• Nexa or Montserrat or similar

Requirements
Should not have
• Avoid cartoon styles, clipart, or anything that looks cheap

```html
<!DOCTYPE html>
<html lang="en">
<head>
<meta charset="utf-8">
<title>Stone Well – Banner Set</title>
<link rel="stylesheet" href="https://fonts.googleapis.com/css2?family=Montserrat:wght@400;500;600;700;800&display=swap">
<style>
:root{
  --board:#9b9b9b;
  --navy:#0b1a2b;
  --navy-lead:#0d2d49;
  --chip:#173452;
  --blue:#2f74cc;
  --blue-bright:#3a82d8;
  --ink:#1b2c3d;
  --white:#ffffff;
  --label:#141414;
}
*{margin:0;padding:0;box-sizing:border-box}
html,body{width:1200px;height:980px;overflow:hidden;background:var(--board);font-family:"Montserrat",Arial,sans-serif}
.canvas{position:relative;width:1200px;height:980px}
.size-label{position:absolute;font-size:15px;font-weight:400;color:var(--label);white-space:nowrap}
.ad{position:absolute;overflow:hidden;background:var(--navy);box-shadow:0 4px 10px rgba(0,0,0,.25)}
.ad > *{position:absolute}
.header{left:0;top:0;background:var(--white)}
.photo{background:linear-gradient(180deg,#4b5d82 0%,#6d7ea3 30%,#3a3730 58%,#8a6a3e 72%,#2a2a2c 88%,#4a4c52 100%)}
.panel{background:var(--navy)}
.stripe{background:var(--blue)}
.brand{display:flex;align-items:center;color:var(--ink)}
.brand-mark{background:#123553;flex:none}
.brand-name{font-weight:600;color:var(--ink);white-space:nowrap;line-height:1}
.brand-tag{font-weight:700;color:var(--blue);white-space:nowrap;letter-spacing:.02em;line-height:1}
.compare{font-weight:800;color:var(--blue);text-align:center;line-height:1;letter-spacing:.01em}
.benefit{display:flex;align-items:center;color:var(--white);font-weight:500;white-space:nowrap;line-height:1}
.chip{border-radius:50%;background:var(--chip);display:flex;align-items:center;justify-content:center;flex:none}
.chip svg{width:62%;height:62%}
.headline{font-weight:800;color:var(--white);text-align:center;line-height:1.15}
.rule{height:2px;background:var(--blue)}
.dl-icon{border:1.6px solid var(--blue);border-radius:50%;display:flex;align-items:center;justify-content:center}
.dl-icon svg{width:55%;height:55%}
.cta{background:var(--blue);color:var(--white);font-weight:800;border-radius:999px;display:flex;align-items:center;justify-content:center;white-space:nowrap}
</style>
</head>
<body>
<svg width="0" height="0" style="position:absolute">
  <defs>
    <symbol id="ic-price" viewBox="0 0 24 24"><g fill="none" stroke="#fff" stroke-width="1.5"><circle cx="13" cy="13" r="6"/><path d="M13 10v6M11.3 11.4c.4-.8 3.3-.9 3.3.4s-3.3.8-3.3 2.2 2.9 1.2 3.3.4"/><path d="M3 8l4-4 3 3 4-4"/></g></symbol>
    <symbol id="ic-risk" viewBox="0 0 24 24"><g fill="none" stroke="#fff" stroke-width="1.5"><path d="M5 3h9l3 3v6M5 3v18h7"/><path d="M8 8h6M8 11h5M8 14h3"/><path d="M17 13l5 8h-10z"/><path d="M17 16v2"/></g></symbol>
    <symbol id="ic-scope" viewBox="0 0 24 24"><g fill="none" stroke="#fff" stroke-width="1.5"><path d="M6 5H4v16h11"/><path d="M8 3h6v3H8z"/><circle cx="15" cy="13" r="5"/><circle cx="15" cy="13" r="2"/><path d="M15 13l6-6"/></g></symbol>
    <symbol id="ic-value" viewBox="0 0 24 24"><g fill="none" stroke="#fff" stroke-width="1.5"><path d="M4 21v-3M8 21v-5M12 21v-7M16 21v-9M20 21v-11"/><path d="M4 14l6-4 3 2 7-8M16 4h4v4"/></g></symbol>
    <symbol id="ic-download" viewBox="0 0 24 24"><g fill="none" stroke="#3a82d8" stroke-width="1.8" stroke-linecap="round" stroke-linejoin="round"><path d="M12 3v13M6 11l6 6 6-6M5 21h14"/></g></symbol>
  </defs>
</svg>

<main class="canvas">

  <!-- Skyscraper 300x600 -->
  <p class="size-label" style="left:74px;top:75px">Desktop Banner ad: (300x600 pixels)</p>
  <section class="ad ad-skyscraper" style="left:74px;top:103px;width:296px;height:592px">
    <div class="header" style="width:296px;height:86px"></div>
    <div class="brand" style="left:34px;top:20px;gap:10px">
      <span class="brand-mark" style="width:14px;height:14px"></span>
      <div>
        <p class="brand-name" style="font-size:26px">Stone Well</p>
        <p class="brand-tag" style="font-size:6.5px;margin-top:5px">COMPARE QUOTES FROM TRUSTED BUILDERS</p>
      </div>
    </div>
    <div class="photo" role="img" aria-label="Modern two-storey home with warm lit windows at dusk" style="left:0;top:86px;width:296px;height:220px"></div>
    <div class="stripe" style="left:0;top:0;width:296px;height:592px;clip-path:polygon(0 294px,296px 234px,296px 244px,0 303px)"></div>
    <div class="panel" style="left:0;top:0;width:296px;height:592px;clip-path:polygon(0 303px,296px 244px,296px 592px,0 592px)"></div>
    <p class="compare" style="left:0;top:306px;width:296px;font-size:23px">COMPARE</p>
    <div class="benefit" style="left:38px;top:337px;gap:6px;font-size:19px"><span class="chip" style="width:32px;height:32px"><svg><use href="#ic-price"/></svg></span>PRICE</div>
    <div class="benefit" style="left:154px;top:337px;gap:6px;font-size:19px"><span class="chip" style="width:32px;height:32px"><svg><use href="#ic-scope"/></svg></span>SCOPE</div>
    <div class="benefit" style="left:38px;top:376px;gap:6px;font-size:19px"><span class="chip" style="width:32px;height:32px"><svg><use href="#ic-risk"/></svg></span>RISK</div>
    <div class="benefit" style="left:154px;top:376px;gap:6px;font-size:19px"><span class="chip" style="width:32px;height:32px"><svg><use href="#ic-value"/></svg></span>VALUE</div>
    <p class="headline" style="left:0;top:430px;width:296px;font-size:21px">BUILD WITH<br>CONFIDENCE</p>
    <div class="rule" style="left:114px;top:483px;width:68px"></div>
    <div class="dl-icon" style="left:132px;top:495px;width:33px;height:33px"><svg><use href="#ic-download"/></svg></div>
    <div class="cta" style="left:70px;top:537px;width:157px;height:31px;font-size:13.5px">DOWNLOAD FREE</div>
  </section>

  <!-- Medium Rectangle 300x250 -->
  <p class="size-label" style="left:408px;top:75px">Medium Rectangle: 300 × 250 pixels</p>
  <section class="ad ad-rectangle" style="left:408px;top:103px;width:296px;height:246px">
    <div class="header" style="width:296px;height:55px"></div>
    <div class="brand" style="left:12px;top:17px;gap:7px">
      <span class="brand-mark" style="width:9px;height:9px"></span>
      <div>
        <p class="brand-name" style="font-size:16.5px">Stone Well</p>
        <p class="brand-tag" style="font-size:4.2px;margin-top:3px">COMPARE QUOTES FROM TRUSTED BUILDERS</p>
      </div>
    </div>
    <div class="photo" role="img" aria-label="Modern two-storey home with warm lit windows at dusk" style="left:0;top:55px;width:190px;height:191px"></div>
    <div class="stripe" style="left:0;top:0;width:296px;height:246px;clip-path:polygon(169px 55px,177px 55px,137px 246px,129px 246px)"></div>
    <div class="panel" style="left:0;top:0;width:296px;height:246px;clip-path:polygon(179px 0,296px 0,296px 246px,137px 246px)"></div>
    <p class="compare" style="left:180px;top:14px;width:102px;font-size:15.5px">COMPARE</p>
    <div class="benefit" style="left:200px;top:35px;gap:5px;font-size:13px"><span class="chip" style="width:20px;height:20px"><svg><use href="#ic-price"/></svg></span>PRICE</div>
    <div class="benefit" style="left:200px;top:61px;gap:5px;font-size:13px"><span class="chip" style="width:20px;height:20px"><svg><use href="#ic-risk"/></svg></span>RISK</div>
    <div class="benefit" style="left:200px;top:87px;gap:5px;font-size:13px"><span class="chip" style="width:20px;height:20px"><svg><use href="#ic-scope"/></svg></span>SCOPE</div>
    <div class="benefit" style="left:200px;top:113px;gap:5px;font-size:13px"><span class="chip" style="width:20px;height:20px"><svg><use href="#ic-value"/></svg></span>VALUE</div>
    <p class="headline" style="left:160px;top:141px;width:126px;font-size:14px">BUILD WITH<br>CONFIDENCE</p>
    <div class="rule" style="left:199px;top:176px;width:46px;height:1.5px"></div>
    <div class="dl-icon" style="left:211px;top:184px;width:22px;height:22px;border-width:1.2px"><svg><use href="#ic-download"/></svg></div>
    <div class="cta" style="left:173px;top:212px;width:99px;height:20px;font-size:8.5px">DOWNLOAD FREE</div>
  </section>

  <!-- Leaderboard 728x90 -->
  <p class="size-label" style="left:408px;top:377px">Leaderboard: 728 × 90 pixels</p>
  <section class="ad ad-leaderboard" style="left:408px;top:405px;width:719px;height:89px">
    <div class="header" style="width:212px;height:89px"></div>
    <div class="brand" style="left:22px;top:34px;gap:8px">
      <span class="brand-mark" style="width:10px;height:10px"></span>
      <div>
        <p class="brand-name" style="font-size:20px">Stone Well</p>
        <p class="brand-tag" style="font-size:5.2px;margin-top:3px">COMPARE QUOTES FROM TRUSTED BUILDERS</p>
      </div>
    </div>
    <div class="photo" role="img" aria-label="Modern two-storey home with warm lit windows at dusk" style="left:212px;top:0;width:204px;height:89px"></div>
    <div class="stripe" style="left:0;top:0;width:719px;height:89px;clip-path:polygon(406px 0,413px 0,396px 89px,389px 89px)"></div>
    <div class="panel" style="left:0;top:0;width:719px;height:89px;background:var(--navy-lead);clip-path:polygon(413px 0,719px 0,719px 89px,396px 89px)"></div>
    <p class="compare" style="left:450px;top:12px;width:100px;font-size:15px">COMPARE</p>
    <div class="benefit" style="left:432px;top:32px;gap:7px;font-size:12.5px"><svg width="14" height="14"><use href="#ic-price"/></svg>PRICE</div>
    <div class="benefit" style="left:508px;top:32px;gap:7px;font-size:12.5px"><svg width="14" height="14"><use href="#ic-scope"/></svg>SCOPE</div>
    <div class="benefit" style="left:432px;top:58px;gap:7px;font-size:12.5px"><svg width="14" height="14"><use href="#ic-risk"/></svg>RISK</div>
    <div class="benefit" style="left:508px;top:58px;gap:7px;font-size:12.5px"><svg width="14" height="14"><use href="#ic-value"/></svg>VALUE</div>
    <p class="headline" style="left:600px;top:10px;width:90px;font-size:10px;line-height:1.2">BUILD WITH<br>CONFIDENCE</p>
    <div class="rule" style="left:630px;top:37px;width:30px;height:1px"></div>
    <div class="dl-icon" style="left:636px;top:42px;width:17px;height:17px;border-width:1px"><svg><use href="#ic-download"/></svg></div>
    <div class="cta" style="left:607px;top:63px;width:78px;height:14px;font-size:6.2px">DOWNLOAD FREE</div>
  </section>

  <!-- Desktop 640x360 -->
  <p class="size-label" style="left:408px;top:521px">Desktop Banner ad image: (640x360 pixels)</p>
  <section class="ad ad-desktop" style="left:408px;top:550px;width:631px;height:355px">
    <div class="header" style="width:347px;height:79px"></div>
    <div class="brand" style="left:66px;top:22px;gap:10px">
      <span class="brand-mark" style="width:13px;height:13px"></span>
      <div>
        <p class="brand-name" style="font-size:28px">Stone Well</p>
        <p class="brand-tag" style="font-size:6.8px;margin-top:5px">COMPARE QUOTES FROM TRUSTED BUILDERS</p>
      </div>
    </div>
    <div class="photo" role="img" aria-label="Modern two-storey home with warm lit windows at dusk" style="left:0;top:79px;width:336px;height:276px"></div>
    <div class="stripe" style="left:0;top:0;width:631px;height:355px;clip-path:polygon(323px 79px,334px 79px,282px 355px,271px 355px)"></div>
    <div class="panel" style="left:0;top:0;width:631px;height:355px;clip-path:polygon(347px 0,631px 0,631px 355px,282px 355px)"></div>
    <p class="compare" style="left:385px;top:36px;width:200px;font-size:25px">COMPARE</p>
    <div class="benefit" style="left:366px;top:69px;gap:8px;font-size:20px"><span class="chip" style="width:34px;height:34px"><svg><use href="#ic-price"/></svg></span>PRICE</div>
    <div class="benefit" style="left:491px;top:69px;gap:8px;font-size:20px"><span class="chip" style="width:34px;height:34px"><svg><use href="#ic-scope"/></svg></span>SCOPE</div>
    <div class="benefit" style="left:366px;top:111px;gap:8px;font-size:20px"><span class="chip" style="width:34px;height:34px"><svg><use href="#ic-risk"/></svg></span>RISK</div>
    <div class="benefit" style="left:491px;top:111px;gap:8px;font-size:20px"><span class="chip" style="width:34px;height:34px"><svg><use href="#ic-value"/></svg></span>VALUE</div>
    <p class="headline" style="left:385px;top:170px;width:200px;font-size:23.5px">BUILD WITH<br>CONFIDENCE</p>
    <div class="rule" style="left:449px;top:227px;width:73px"></div>
    <div class="dl-icon" style="left:468px;top:240px;width:35px;height:35px;border-width:1.8px"><svg><use href="#ic-download"/></svg></div>
    <div class="cta" style="left:402px;top:286px;width:170px;height:34px;font-size:15px">DOWNLOAD FREE</div>
  </section>

</main>
</body>
</html>
```